Milo Brennick Design, LLC: Die-Cut/Industrial Architecture Work

I have uploaded an amazing business card design which will be printed on stainless steel (metal). The logo does not need to change nor the card layout except as may be necessary to complete the project I am about to describe. THIS IS A DIE-CUT and STEEL BEAM IMAGERY PROJECT.

I am an architect and much of my work is steel structures. This business card project is focused exclusively taking the card design ("as is") to the next level of incredible by incorporating some type of die-cutting or creative imagery (maybe even abstract) of a steel beam which signifies the type of industrial architecture I do. Ultimately, when someone looks at this business card ... I want the card to have an "industrial" feel and it obvious that I do steel structures.

```html
<!DOCTYPE html>
<html lang="en">
<head>
<meta charset="utf-8">
<title>Milo Brennick Design, LLC — Business Card</title>
<link rel="stylesheet" href="https://fonts.googleapis.com/css2?family=Outfit:wght@400;600&display=swap">
<style>
  :root {
    --backdrop: #d6b083;
    --cut-shadow: #6b5236;
    --steel-light: #eceded;
    --steel-mid: #cfd1d2;
    --steel-dark: #b7babc;
    --ink: #161616;
    --ink-soft: #3c3c3c;
    --engrave: #9ea2a5;
  }
  * { box-sizing: border-box; margin: 0; padding: 0; }
  html, body { width: 1093px; height: 1200px; overflow: hidden; }
  body {
    background: var(--backdrop);
    font-family: "Outfit", sans-serif;
    position: relative;
  }
  .card {
    position: absolute;
    left: 190px;
    width: 729px;
    height: 449px;
    border-radius: 24px;
    overflow: hidden;
    background:
      repeating-linear-gradient(180deg, rgba(255,255,255,0.18) 0 1px, rgba(0,0,0,0.035) 1px 3px),
      linear-gradient(180deg, var(--steel-mid) 0%, var(--steel-light) 22%, var(--steel-dark) 50%, var(--steel-light) 78%, var(--steel-mid) 100%);
  }
  .card--front { top: 127px; }
  .card--back { top: 640px; }

  /* die-cut steel I-beam cross-section */
  .beam-cut {
    position: absolute;
    width: 246px;
    height: 263px;
  }
  .beam-cut__shape { fill: var(--backdrop); }
  .beam-cut__edge { fill: none; stroke: var(--cut-shadow); stroke-width: 3; opacity: 0.55; }
  .card--front .beam-cut { left: 467px; top: 90px; }
  .card--back .beam-cut { left: 18px; top: 89px; }

  .lockup {
    position: absolute;
    left: 65px;
    top: 158px;
    height: 126px;
    display: flex;
    align-items: center;
    gap: 18px;
  }
  .lockup__square { width: 44px; height: 44px; background: var(--ink); }
  .lockup__rule { width: 2px; height: 126px; background: var(--ink); }
  .lockup__name {
    font-weight: 400;
    font-size: 25px;
    letter-spacing: 0.5px;
    color: var(--ink);
    white-space: nowrap;
  }
  .tagline {
    position: absolute;
    left: 61px;
    top: 316px;
    font-weight: 600;
    font-size: 19px;
    color: var(--ink-soft);
    white-space: nowrap;
  }

  .back-name {
    position: absolute;
    left: 290px;
    top: 80px;
    font-weight: 400;
    font-size: 28px;
    color: var(--engrave);
    white-space: nowrap;
  }
  .contact {
    position: absolute;
    left: 304px;
    font-size: 24px;
    line-height: 26px;
    color: var(--ink);
    list-style: none;
  }
  .contact__item {
    display: flex;
    align-items: flex-start;
    gap: 8px;
    white-space: nowrap;
  }
  .contact__icon { width: 22px; height: 22px; flex: none; margin-top: 2px; fill: var(--ink); }
  .contact__icon--globe { fill: none; stroke: var(--ink); stroke-width: 1.8; }
  .contact--address { top: 171px; }
  .contact--lines { top: 287px; }
  .contact--lines .contact__item { margin-bottom: 7px; }
</style>
</head>
<body>

<section class="card card--front" aria-label="Card front">
  <div class="lockup">
    <div class="lockup__square"></div>
    <div class="lockup__rule"></div>
    <div class="lockup__name">Milo Brennick Design, LLC</div>
  </div>
  <p class="tagline">Studio For Creative Architectural Thought</p>
  <svg class="beam-cut" viewBox="0 0 246 263" role="img" aria-label="Die-cut steel I-beam cross-section">
    <path class="beam-cut__shape" d="M4 0H242a4 4 0 0 1 4 4V44a4 4 0 0 1-4 4H150a6 6 0 0 0-6 6V209a6 6 0 0 0 6 6H242a4 4 0 0 1 4 4V259a4 4 0 0 1-4 4H4a4 4 0 0 1-4-4V219a4 4 0 0 1 4-4H96a6 6 0 0 0 6-6V54a6 6 0 0 0-6-6H4a4 4 0 0 1-4-4V4a4 4 0 0 1 4-4z"/>
    <path class="beam-cut__edge" d="M1.5 44V4a3 3 0 0 1 3-3H242M102 54V209"/>
  </svg>
</section>

<section class="card card--back" aria-label="Card back">
  <svg class="beam-cut" viewBox="0 0 246 263" role="img" aria-label="Die-cut steel I-beam cross-section">
    <path class="beam-cut__shape" d="M4 0H242a4 4 0 0 1 4 4V44a4 4 0 0 1-4 4H150a6 6 0 0 0-6 6V209a6 6 0 0 0 6 6H242a4 4 0 0 1 4 4V259a4 4 0 0 1-4 4H4a4 4 0 0 1-4-4V219a4 4 0 0 1 4-4H96a6 6 0 0 0 6-6V54a6 6 0 0 0-6-6H4a4 4 0 0 1-4-4V4a4 4 0 0 1 4-4z"/>
    <path class="beam-cut__edge" d="M1.5 44V4a3 3 0 0 1 3-3H242M102 54V209"/>
  </svg>
  <div class="back-name">Milo Brennick Design, LLC</div>

  <ul class="contact contact--address">
    <li class="contact__item">
      <svg class="contact__icon" viewBox="0 0 24 24"><path d="M12 1a8 8 0 0 0-8 8c0 5.6 8 14 8 14s8-8.4 8-14a8 8 0 0 0-8-8zm0 11a3 3 0 1 1 0-6 3 3 0 0 1 0 6z"/></svg>
      <span>4810 Harbor Pointe Drive<br>Suite 512<br>Tampa FL 33602</span>
    </li>
  </ul>

  <ul class="contact contact--lines">
    <li class="contact__item">
      <svg class="contact__icon" viewBox="0 0 24 24"><path d="M6.6 10.8a15.2 15.2 0 0 0 6.6 6.6l2.2-2.2c.3-.3.7-.4 1-.2 1.1.4 2.3.6 3.6.6.6 0 1 .4 1 1V20c0 .6-.4 1-1 1A17 17 0 0 1 3 4c0-.6.4-1 1-1h3.5c.6 0 1 .4 1 1 0 1.3.2 2.5.6 3.6.1.3 0 .7-.2 1z"/></svg>
      <span>813.555.0148</span>
    </li>
    <li class="contact__item">
      <svg class="contact__icon" viewBox="0 0 24 24"><path d="M2 5h20v14H2zm2 2v.5l8 5.5 8-5.5V7l-8 5.5z"/></svg>
      <span>milo@milobrennick.design</span>
    </li>
    <li class="contact__item">
      <svg class="contact__icon contact__icon--globe" viewBox="0 0 24 24"><circle cx="12" cy="12" r="9.5"/><ellipse cx="12" cy="12" rx="4.2" ry="9.5"/><path d="M2.5 12h19M4 7h16M4 17h16"/></svg>
      <span>www.milobrennick.design</span>
    </li>
  </ul>
</section>

</body>
</html>
```